Application for baby milk and water counter

We are building baby food app. Need to design main screen for tha app first so we can go forward to other secondary screens of the app

Food dashboard screen
Food dashboard screen is main page for view/edit food data

General vision
I see the app in pastel colors with some illustrations to make the app more in positive. You can influence from game Lantern Hollow. I see with smooth colors and gradients like in a game. Also need to have animations/transitions for each action. Each click should create smooth transition to new state. My idea is to build one dashboard screen for food which we can reuse it for other screens. So a lot of thinking should go into design stage to app appealing.

Food Dashboard
Current screen should show all the data about food intake of the baby. So here user should see

Milk How much food baby had in ml/oz. So there should be some kind of illustrated bottle or glass or smth that shows it is filled with that amount.

Add/Remove controls for food. Should be some kind of custom control for inputing amount to remove/add. I see it as a slider on the side of the bottle. User slides up or down and amount is added/removed.

Notification. So user should be aware how many hours/minutes left for next food intake. This is optional field, so consider it could be disabled. So no empty space should be on a screen. There should be human readable text. Something like. 1:30 minutes left for next intake. Maybe could be some custom made icons to illustrate that it is next food intake.

Burped: User should have ability to how much baby burped. This amount is integer value. So it could be “Baby burped 2 times today”. So again here I see some custom made/icon to illustrate how many times baby burped and amount next to it. I see changing the value just by tapping, but I don’t know how to edit if user tapped accidentally more than it should be. So TBD here.

Date and time: Dashboard should show for which date it is viewing/editing data. Should be able to change it, so user can add/edit data for yesterday. Don’t want to see here calendar on a screen so need to come up with nice design decision.

Water: User should have ability to view/edit water intake of the baby, but water is secondary information so it should be smaller than milk, or come up with some other idea how to show the water. I see to have same controls for water like for milk. Water intake is optional it can be disabled by the user.

Target Market(s)

For just became mothers

Font styles to use
Sans Serif

Colors
0094D4
00A9DD
6FCCEA
C7EBF8
E9F6FB
FFC000
F8CF3A
FAE287
FDF2CF
FEFAEE
E54698
E96AAD
F1A4CE
F9D9EA
FCEFF6

Requirements
Must have
• Ilustrations or playfull icons for show information

```html
<!DOCTYPE html>
<html lang="en">
<head>
<meta charset="UTF-8">
<title>Food Dashboard – Milk</title>
<link rel="stylesheet" href="https://fonts.googleapis.com/css2?family=Poppins:wght@400;500;600&display=swap">
<style>
  :root {
    --stage: #111111;
    --yellow-deep: #FFC000;
    --yellow: #F8CF3A;
    --yellow-soft: #FAE287;
    --yellow-pale: #FDF2CF;
    --screen-top: #FDD862;
    --screen-mid: #F8BE6E;
    --pink-deep: #E54698;
    --pink: #E96AAD;
    --pink-soft: #F1A4CE;
    --pink-pale: #F9D9EA;
    --white: #FFFFFF;
  }
  * { box-sizing: border-box; margin: 0; padding: 0; }
  html, body {
    width: 1200px; height: 1200px; overflow: hidden;
    background: var(--stage);
    font-family: "Poppins", sans-serif;
  }
  .screen {
    position: absolute; left: 346px; top: 51px;
    width: 507px; height: 1098px;
    border-radius: 56px; overflow: hidden;
    background: linear-gradient(180deg, var(--screen-top) 0%, var(--screen-top) 45%, var(--screen-mid) 68%, var(--pink) 100%);
  }
  .date-nav { position: absolute; top: 61px; left: 0; width: 100%; height: 51px; }
  .date-nav__arrow { position: absolute; top: 12px; width: 28px; height: 28px; }
  .date-nav__arrow--prev { left: 38px; }
  .date-nav__arrow--next { right: 38px; }
  .date-nav__pill {
    position: absolute; left: 104px; width: 300px; height: 51px;
    border-radius: 26px; background: var(--yellow-pale);
    opacity: 0.85;
    display: flex; align-items: center; justify-content: center;
    color: var(--pink-deep); font-size: 20px; font-weight: 400;
  }
  .intake-title {
    position: absolute; top: 134px; width: 100%; text-align: center;
    color: var(--pink-deep); font-size: 28px; font-weight: 500; letter-spacing: 0.5px;
  }
  .intake-hint {
    position: absolute; top: 172px; width: 100%; text-align: center;
    color: var(--white); font-size: 16px; font-weight: 400;
  }
  .bottle {
    position: absolute; left: 86px; top: 226px; width: 336px; height: 495px;
  }
  .bottle__art {
    position: absolute; left: 38px; top: 0; width: 260px; height: 495px;
    border-radius: 110px 110px 90px 90px;
    background: linear-gradient(180deg, var(--pink) 0%, var(--pink) 30%, var(--pink-pale) 45%, var(--white) 55%, var(--white) 100%);
    border: 18px solid var(--pink);
    box-shadow: 0 0 30px rgba(255, 192, 0, 0.55);
  }
  .bottle__readout {
    position: absolute; left: 92px; top: 285px; width: 152px; height: 152px;
    border-radius: 50%; background: var(--pink);
    border: 7px solid var(--yellow-deep);
    display: flex; flex-direction: column; align-items: center; justify-content: center;
    color: var(--white); font-weight: 600; line-height: 1;
  }
  .bottle__amount { font-size: 56px; }
  .bottle__unit { font-size: 34px; margin-top: 2px; }
  .amount-slider { position: absolute; left: 60px; top: 759px; width: 385px; height: 12px; }
  .amount-slider__track { position: absolute; top: 3px; left: 0; width: 100%; height: 4px; border-radius: 2px; background: var(--white); }
  .amount-slider__fill { position: absolute; top: 3px; left: 0; width: 285px; height: 4px; border-radius: 2px; background: var(--pink); }
  .amount-slider__thumb {
    position: absolute; left: 270px; top: -10px; width: 30px; height: 30px;
    border-radius: 50%; background: var(--pink); border: 2px solid var(--pink-soft);
  }
  .burp-controls { position: absolute; top: 813px; left: 0; width: 100%; height: 102px; }
  .burp-controls__step {
    position: absolute; top: 24px; width: 54px; height: 54px; border-radius: 50%;
    background: var(--yellow-soft);
  }
  .burp-controls__step--minus { left: 111px; }
  .burp-controls__step--plus { left: 339px; }
  .burp-controls__step svg { width: 54px; height: 54px; }
  .burp-controls__badge {
    position: absolute; left: 201px; top: 0; width: 102px; height: 102px; border-radius: 50%;
    background: var(--yellow-soft); border: 8px solid var(--yellow-pale);
  }
  .burp-controls__badge-art {
    position: absolute; inset: 8px; border-radius: 50%; background: var(--pink-soft);
  }
  .burp-count {
    position: absolute; top: 928px; width: 100%; text-align: center;
    color: var(--white); font-size: 21px; font-weight: 500;
  }
  .next-intake {
    position: absolute; left: 45px; top: 981px; width: 417px; height: 73px;
    border-radius: 18px; background: var(--yellow-soft);
    display: flex; align-items: center; justify-content: center;
    color: var(--pink-deep); font-size: 21px; font-weight: 500;
  }
</style>
</head>
<body>
  <main class="screen">
    <nav class="date-nav">
      <svg class="date-nav__arrow date-nav__arrow--prev" viewBox="0 0 28 28" aria-label="Previous day"><path d="M17 5 L8 14 L17 23" fill="none" stroke="#FFFFFF" stroke-width="3.5" stroke-linecap="round" stroke-linejoin="round"/></svg>
      <div class="date-nav__pill">Tuesday - 05/30/2023</div>
      <svg class="date-nav__arrow date-nav__arrow--next" viewBox="0 0 28 28" aria-label="Next day"><path d="M11 5 L20 14 L11 23" fill="none" stroke="#FFFFFF" stroke-width="3.5" stroke-linecap="round" stroke-linejoin="round"/></svg>
    </nav>

    <h1 class="intake-title">MILK</h1>
    <p class="intake-hint">Swipe left to see Water data</p>

    <section class="bottle">
      <div class="bottle__art" role="img" aria-label="Illustrated baby bottle with handles, partly filled with milk"></div>
      <div class="bottle__readout">
        <span class="bottle__amount">152</span>
        <span class="bottle__unit">ml</span>
      </div>
    </section>

    <div class="amount-slider" aria-label="Milk amount">
      <div class="amount-slider__track"></div>
      <div class="amount-slider__fill"></div>
      <div class="amount-slider__thumb"></div>
    </div>

    <div class="burp-controls">
      <div class="burp-controls__step burp-controls__step--minus">
        <svg viewBox="0 0 54 54" aria-label="Remove burp"><rect x="18" y="25" width="18" height="4" rx="2" fill="#E96AAD"/></svg>
      </div>
      <div class="burp-controls__badge">
        <div class="burp-controls__badge-art" role="img" aria-label="Playful burp icon"></div>
      </div>
      <div class="burp-controls__step burp-controls__step--plus">
        <svg viewBox="0 0 54 54" aria-label="Add burp"><rect x="18" y="25" width="18" height="4" rx="2" fill="#E96AAD"/><rect x="25" y="18" width="4" height="18" rx="2" fill="#E96AAD"/></svg>
      </div>
    </div>

    <p class="burp-count">Baby burped 2 times today!</p>

    <div class="next-intake">2 Hrs 35 mins Till Next Intake</div>
  </main>
</body>
</html>
```